Zebra Romp - mobile play centre poster designs

Who are we - we are a mobile playground business that specialises in providing entertainment to children in a safe, clean environment either at home or in a function centre. Brief - create 4 different signs to be displayed on our playgrounds. Please find attached 3 photos from our competitors to use as a guide. Corflute sign - size A1 Toddler zone - size A1 Playground rules - size A4 No climbing - size 20cmx8cm sending through photos and documents now.
Colors
Designer to choose colors to be used in the design.
Requirements
Must have
- Colour, be very specific with the rules, pictures

```html
<!DOCTYPE html>
<html lang="en">
<head>
<meta charset="utf-8">
<title>Zebra Romp – Playground Signs</title>
<link href="https://fonts.googleapis.com/css2?family=Arimo:wght@400;700&display=swap" rel="stylesheet">
<style>
  :root {
    --red: #ed2024;
    --ink: #111111;
    --grey: #6d6e71;
    --white: #ffffff;
    --mascot: #c98a3d;
    --art: #9a9a9a;
  }
  * { margin: 0; padding: 0; box-sizing: border-box; }
  html, body { width: 1200px; height: 970px; overflow: hidden; background: var(--white); }
  body { font-family: "Arimo", Arial, sans-serif; color: var(--ink); }
  .board { position: relative; width: 1200px; height: 970px; }

  .sign { position: absolute; background: var(--white); border: 16px solid var(--red); }
  .sign--age { left: 90px; top: 94px; width: 523px; height: 370px; }
  .sign--toddler { left: 90px; top: 506px; width: 523px; height: 370px; }
  .sign--rules { left: 709px; top: 94px; width: 402px; height: 568px; border-width: 13px; }
  .sign--climb { left: 709px; top: 715px; width: 402px; height: 160px; border-width: 8px; }

  .brand { position: absolute; left: 0; right: 0; display: flex; justify-content: center; align-items: center; gap: 10px; }
  .brand__text { display: flex; flex-direction: column; align-items: flex-start; }
  .brand__name { font-weight: 700; color: var(--red); font-size: 36px; letter-spacing: 1px; line-height: 1; }
  .brand__tag { color: var(--grey); font-size: 14px; letter-spacing: 1px; margin-top: 6px; }
  .brand__mark { width: 44px; height: 44px; border-radius: 50%; background: var(--mascot); }

  .sign--age .brand, .sign--toddler .brand { top: 40px; }
  .sign--rules .brand { top: 30px; }
  .sign--rules .brand__name { font-size: 34px; }

  .headline { position: absolute; left: 0; right: 0; text-align: center; font-weight: 700; color: var(--red); }
  .sign--age .headline { top: 150px; font-size: 38px; text-shadow: 1px 1px 0 #b9b9b9; }

  .note { position: absolute; left: 55px; display: flex; align-items: center; font-weight: 700; font-size: 17px; }
  .note__icon { width: 50px; display: flex; justify-content: center; margin-right: 12px; }
  .note--supervise { top: 246px; }
  .note--socks { top: 296px; }
  .hl { color: var(--red); }
  .placeholder-figure { width: 48px; height: 40px; background: var(--art); border-radius: 4px; }

  .toddler-copy { position: absolute; top: 134px; left: 20px; right: 20px; text-align: center; font-weight: 700; font-size: 14.5px; line-height: 24.6px; }
  .toddler-copy .lead { color: var(--red); }

  .supervise-copy { position: absolute; top: 128px; left: 0; right: 0; text-align: center; font-weight: 700; font-size: 13.5px; line-height: 21px; }
  .sign--rules .headline { top: 166px; font-size: 30px; text-shadow: 1px 1px 0 #b9b9b9; }
  .rules { position: absolute; top: 232px; left: 28px; list-style: none; }
  .rule { display: flex; align-items: center; height: 43.5px; font-weight: 700; font-size: 13px; }
  .rule__icon { width: 34px; display: flex; justify-content: center; margin-right: 31px; }
  .rule__no { color: var(--red); font-size: 18px; margin-right: 6px; font-weight: 400; }
  .face-spot { width: 26px; height: 26px; border-radius: 50%; background: var(--art); }

  .climb-art { position: absolute; left: 15px; top: 41px; width: 72px; height: 72px; }
  .climb-art__fill { position: absolute; inset: 0; background: var(--art); }
  .climb-art svg { position: absolute; left: -6px; top: -4px; }
  .climb-title { position: absolute; left: 110px; top: 34px; font-weight: 700; font-size: 39px; white-space: nowrap; text-shadow: 1px 1px 0 #b9b9b9; }
  .climb-title .hl { margin-right: 6px; }
  .sign--climb .brand { top: 96px; left: 110px; right: 0; gap: 5px; }
  .sign--climb .brand__name { font-size: 16px; letter-spacing: 0; }
  .sign--climb .brand__tag { font-size: 7px; margin-top: 2px; }
  .sign--climb .brand__mark { width: 20px; height: 20px; }
</style>
</head>
<body>
<main class="board">

  <section class="sign sign--age">
    <div class="brand">
      <div class="brand__text"><span class="brand__name">ZEBRA ROMP</span><span class="brand__tag">MOBILE PLAY CENTRE</span></div>
      <span class="brand__mark"></span>
    </div>
    <h1 class="headline">0-3 YEAR OLDS ONLY</h1>
    <p class="note note--supervise">
      <span class="note__icon"><span class="placeholder-figure" role="img" aria-label="Pictogram of an adult supervising a crawling baby"></span></span>
      <span><span class="hl">SUPERVISION</span> REQUIRED AT ALL TIMES</span>
    </p>
    <p class="note note--socks">
      <span class="note__icon">
        <svg width="32" height="36" viewBox="0 0 32 36" aria-hidden="true">
          <path d="M4 2h10v16l6 6a5 5 0 0 1-7 7L5 23a4 4 0 0 1-1-3z" fill="#111"/>
          <path d="M16 4h10v16l4 4a5 5 0 0 1-7 7l-4-4" fill="#111" stroke="#fff" stroke-width="1.5"/>
        </svg>
      </span>
      <span>PARENTS PLEASE <span class="hl">WEAR SOCKS</span> TOO</span>
    </p>
  </section>

  <section class="sign sign--toddler">
    <div class="brand">
      <div class="brand__text"><span class="brand__name">ZEBRA ROMP</span><span class="brand__tag">MOBILE PLAY CENTRE</span></div>
      <span class="brand__mark"></span>
    </div>
    <p class="toddler-copy">
      <span class="lead">IF USING THE TODDLER SOFT PLAY EQUIPMENT,</span><br>
      PLEASE ENSURE THAT THIS AREA IS USED BY<br>
      CHILDREN&nbsp; <span class="lead">0-3 ONLY.</span>&nbsp; THE EQUIPMENT AND BALL<br>
      PIT IS ONLY DESIGNED FOR SMALL CHILDREN AND<br>
      BIGGER KIDS MIGHT INJURE THEMSELVES, THE<br>
      SMALLER CHILDREN OR CAUSE EXTENSIVE<br>
      DAMAGE TO THE EQUIPMENT, OF WHICH THERE<br>
      WILL BE A CHARGE BACK TO THE CLIENT.
    </p>
  </section>

  <section class="sign sign--rules">
    <div class="brand">
      <div class="brand__text"><span class="brand__name">ZEBRA ROMP</span><span class="brand__tag">MOBILE PLAY CENTRE</span></div>
      <span class="brand__mark"></span>
    </div>
    <p class="supervise-copy">Parents/Guardians must supervise children<br>using this play equipment at all times</p>
    <h2 class="headline">PLAY GROUND RULES</h2>
    <ul class="rules">
      <li class="rule"><span class="rule__icon"><svg width="30" height="30" viewBox="0 0 30 30" aria-hidden="true"><g fill="none" stroke="#111" stroke-width="2"><path d="M4 5c0-3 8-3 8 0v20c0 4-8 4-8 0z"/><path d="M18 5c0-3 8-3 8 0v20c0 4-8 4-8 0z"/></g></svg></span><span class="rule__no">NO</span>SHOES – SOCKS MUST BE WORN</li>
      <li class="rule"><span class="rule__icon"><svg width="30" height="30" viewBox="0 0 30 30" aria-hidden="true"><g fill="none" stroke="#111" stroke-width="1.5"><rect x="3" y="3" width="24" height="24"/><path d="M3 9l18 18M3 15l12 12M3 21l6 6M9 3l18 18M15 3l12 12M21 3l6 6M27 9L9 27M27 15L15 27M27 21l-6 6M21 3L3 21M15 3L3 15M9 3L3 9"/></g></svg></span><span class="rule__no">NO</span>CLIMBING THE NETS</li>
      <li class="rule"><span class="rule__icon"><svg width="30" height="30" viewBox="0 0 30 30" aria-hidden="true"><g fill="none" stroke="#111" stroke-width="2"><path d="M6 8h10l-2 18H8z"/><path d="M11 8l2-6h4"/><rect x="14" y="16" width="13" height="4" rx="2"/><rect x="14" y="21" width="13" height="4" rx="2"/></g></svg></span><span class="rule__no">NO</span>FOOD OR DRINK</li>
      <li class="rule"><span class="rule__icon"><svg width="30" height="30" viewBox="0 0 30 30" aria-hidden="true"><g fill="none" stroke="#111" stroke-width="2"><path d="M9 2h4v5l3 4v17H6V11l3-4z"/><path d="M18 16h9v12h-9z"/><path d="M22 16v-4l3-2"/></g></svg></span><span class="rule__no">NO</span>BOTTLE OR GLASS</li>
      <li class="rule"><span class="rule__icon"><svg width="30" height="30" viewBox="0 0 30 30" aria-hidden="true"><g fill="none" stroke="#111" stroke-width="2"><circle cx="12" cy="10" r="7"/><circle cx="10" cy="20" r="7"/><circle cx="20" cy="20" r="7"/></g></svg></span><span class="rule__no">NO</span>CHEWING GUM</li>
      <li class="rule"><span class="rule__icon"><svg width="30" height="30" viewBox="0 0 30 30" aria-hidden="true"><g stroke="#111" stroke-width="3" stroke-linecap="round"><path d="M4 4l22 22"/><path d="M26 4L4 26"/></g></svg></span><span class="rule__no">NO</span>SHARP OBJECTS</li>
      <li class="rule"><span class="rule__icon"><span class="face-spot" role="img" aria-label="Face painting pictogram"></span></span><span class="rule__no">NO</span>FACE PAINTING</li>
    </ul>
  </section>

  <section class="sign sign--climb">
    <div class="climb-art">
      <div class="climb-art__fill" role="img" aria-label="Illustration of a child climbing a play net"></div>
      <svg width="84" height="80" viewBox="0 0 84 80" aria-hidden="true"><line x1="2" y1="78" x2="80" y2="2" stroke="#ed2024" stroke-width="4"/></svg>
    </div>
    <p class="climb-title"><span class="hl">NO</span>CLIMBING</p>
    <div class="brand">
      <div class="brand__text"><span class="brand__name">ZEBRA ROMP</span><span class="brand__tag">MOBILE PLAY CENTRE</span></div>
      <span class="brand__mark"></span>
    </div>
  </section>

</main>
</body>
</html>
```